Need a FLYER/BROCHURE for selling woman hair. I have an online business and need your help.

I need a flyer/BROCHURE that represents my company. We sale hair online and needing for our customers to know our prices and discounts for any holiday and upcoming new year specials. I need the brochure to stand out. Have our brand Logo on it. Pictures of hair we sale on our site and models on the flyer. Prices will need to be place on the flyer indicating before and after the discounts. I also have a bag gift for loyal customers that need to be on the flyer. Colors I am interested in are purple and Gold. Or something creative that will blend with my logo. On my prices I sent. I need to change the title Best, Medium and Low Quality to 6A, 5A, to The Calder Range.

Reason: I would like the deadline to change. The reason I see some designers are coming to my project and some are saying the deadline is too short. I would like to see what they can offer me before I decide.

Industry/Entity Type

Business

Requirements
Must have
• Pictures of my brand. Prices that matches my original prices and sales prices. Pictures of hair and models.

```html
<!DOCTYPE html>
<html lang="en">
<head>
<meta charset="utf-8">
<title>The Calder Range – Price Brochure</title>
<link href="https://fonts.googleapis.com/css2?family=Cinzel:wght@600&family=Great+Vibes&family=Josefin+Sans:wght@300;400&display=swap" rel="stylesheet">
<style>
  :root {
    --bg: #e4e4e6;
    --purple: #55587f;
    --purple-light: #6b6e9a;
    --purple-dark: #474a70;
    --panel: #4d5078;
    --panel-line: #3c3f63;
    --gold: #cf9b34;
    --gold-soft: #e2b75a;
    --ink-light: #e6e6f0;
    --rule: rgba(255,255,255,0.18);
  }
  * { box-sizing: border-box; margin: 0; padding: 0; }
  html, body { width: 1200px; height: 1200px; overflow: hidden; background: var(--bg); }
  body { position: relative; font-family: "Josefin Sans", sans-serif; color: var(--ink-light); }

  .spread { position: absolute; display: flex; box-shadow: 0 6px 16px rgba(0,0,0,0.22); }
  .page {
    position: relative; height: 100%;
    background: radial-gradient(ellipse at 55% 45%, var(--purple-light), var(--purple) 70%);
    overflow: hidden;
  }
  .page + .page { border-left: 1px solid rgba(0,0,0,0.25); }

  .wordmark {
    font-family: "Cinzel", serif; font-weight: 600; color: var(--gold);
    text-align: center; line-height: 1.1; letter-spacing: 0.04em;
  }

  /* cover spread */
  .cover { left: 60px; top: 50px; width: 560px; height: 300px; }
  .cover .page { width: 280px; }
  .cover .wordmark { position: absolute; left: 0; right: 0; top: 120px; font-size: 26px; }
  .contact { position: absolute; left: 0; right: 0; top: 200px; text-align: center; font-size: 10px; font-weight: 300; line-height: 1.6; }
  .website { position: absolute; left: 0; right: 0; bottom: 22px; text-align: center; font-size: 9px; font-weight: 300; }

  /* brand panel */
  .brand-panel {
    position: absolute; left: 708px; top: 56px; width: 492px; height: 333px;
    background: radial-gradient(ellipse at 55% 50%, #7073a0, var(--purple) 70%);
    display: flex; align-items: center; justify-content: center;
  }
  .brand-panel .wordmark { font-size: 42px; }

  /* price tables */
  .panel {
    position: absolute; background: var(--panel);
    border: 1px solid var(--panel-line); padding: 4px 5px;
  }
  .panel-title {
    font-family: "Great Vibes", cursive; color: var(--gold-soft);
    font-size: 15px; line-height: 0.9; text-align: center; margin-bottom: 5px;
  }
  .cols { display: flex; gap: 4px; justify-content: center; }
  .price-table { border-collapse: collapse; font-size: 8px; font-weight: 300; }
  .price-table th { font-weight: 400; font-size: 6.5px; padding: 0 4px 3px; letter-spacing: 0.04em; }
  .price-table td { padding: 0 4px; line-height: 11.5px; }
  .price-table td:first-child { text-align: center; }
  .price-table td + td, .price-table th + th { border-left: 1px solid var(--rule); }

  .photo { position: absolute; }
  .photo-dark { background: radial-gradient(ellipse at 55% 40%, #8a7f92, #3b3344 55%, #6e6f9c 100%); }
  .photo-light { background: radial-gradient(ellipse at 50% 40%, #8d6a5c, #3a2b2c 45%, #efeef0 80%); }
  .photo-blonde { background: radial-gradient(ellipse at 50% 45%, #c79062, #a9704d 45%, #f3f1f0 80%); }
  .photo-bag { background: linear-gradient(180deg, #2b2b2f 0%, #2b2b2f 25%, #c9c6cc 45%, #b4b1b8 80%, #2b2b2f 100%); }

  .prices { left: 580px; top: 450px; width: 580px; height: 340px; }
  .prices .page { width: 290px; }

  .back { left: 40px; top: 820px; width: 600px; height: 320px; }
  .back .page { width: 300px; }
  .gift-note { position: absolute; left: 110px; top: 230px; font-size: 9px; font-weight: 300; }

  .notes-title { position: absolute; left: 0; right: 0; top: 30px; text-align: center; font-family: "Great Vibes", cursive; font-size: 26px; color: var(--gold-soft); }
  .notes-lines { position: absolute; left: 40px; right: 40px; top: 75px; bottom: 30px;
    background: repeating-linear-gradient(180deg, transparent 0 17px, rgba(255,255,255,0.13) 17px 18px); }
  .notes-mark { position: absolute; left: 0; right: 0; top: 150px; font-size: 20px; color: rgba(255,255,255,0.08); }
</style>
</head>
<body>

<section class="spread cover" aria-label="Brochure covers">
  <div class="page back-cover">
    <p class="wordmark">The Calder Range</p>
    <p class="contact">example adress<br>+000 1234 5678<br>example email</p>
    <p class="website">www.yourwebsitehere.com</p>
  </div>
  <div class="page front-cover">
    <p class="wordmark">The Calder Range</p>
  </div>
</section>

<section class="brand-panel" aria-label="Brand">
  <p class="wordmark">The Calder Range</p>
</section>

<section class="spread prices" aria-label="Hair price list">
  <div class="page">
    <div class="photo photo-dark" style="left:95px; top:0; width:195px; height:170px;" role="img" aria-label="Model with long dark curly hair"></div>

    <div class="panel" style="left:5px; top:176px; width:72px; height:158px;">
      <p class="panel-title">high quality</p>
      <div class="cols">
        <table class="price-table">
          <tr><th>INCH</th><th>PRICES</th></tr>
          <tr><td>12</td><td>$55</td></tr><tr><td>14</td><td>$62</td></tr><tr><td>16</td><td>$74</td></tr>
          <tr><td>18</td><td>$81</td></tr><tr><td>20</td><td>$88</td></tr><tr><td>22</td><td>$97</td></tr>
          <tr><td>24</td><td>$107</td></tr><tr><td>26</td><td>$112</td></tr><tr><td>28</td><td>$120</td></tr>
          <tr><td>30</td><td>$128</td></tr>
        </table>
      </div>
    </div>

    <div class="panel" style="left:81px; top:176px; width:124px; height:158px;">
      <p class="panel-title">medium quality</p>
      <div class="cols">
        <table class="price-table">
          <tr><th>INCH</th><th>PRICES</th></tr>
          <tr><td>12</td><td>$43</td></tr><tr><td>14</td><td>$48</td></tr><tr><td>16</td><td>$53</td></tr>
          <tr><td>18</td><td>$59</td></tr><tr><td>20</td><td>$64</td></tr><tr><td>22</td><td>$69</td></tr>
          <tr><td>24</td><td>$80</td></tr><tr><td>26</td><td>$85</td></tr><tr><td>28</td><td>$91</td></tr>
          <tr><td>30</td><td>$96</td></tr>
        </table>
        <table class="price-table">
          <tr><th>INCH</th><th>PRICES</th></tr>
          <tr><td>32</td><td>$98</td></tr><tr><td>34</td><td>$99</td></tr><tr><td>36</td><td>$104</td></tr>
          <tr><td>38</td><td>$107</td></tr><tr><td>40</td><td>$114</td></tr>
        </table>
      </div>
    </div>

    <div class="panel" style="left:209px; top:176px; width:76px; height:158px;">
      <p class="panel-title">low quality</p>
      <div class="cols">
        <table class="price-table">
          <tr><th>INCH</th><th>PRICES</th></tr>
          <tr><td>12</td><td>$29</td></tr><tr><td>14</td><td>$33</td></tr><tr><td>16</td><td>$39</td></tr>
          <tr><td>18</td><td>$42</td></tr><tr><td>20</td><td>$46</td></tr><tr><td>22</td><td>$50</td></tr>
          <tr><td>24</td><td>$54</td></tr><tr><td>26</td><td>$59</td></tr><tr><td>28</td><td>$65</td></tr>
          <tr><td>30</td><td>$81</td></tr>
        </table>
      </div>
    </div>
  </div>

  <div class="page">
    <div class="photo photo-light" style="left:0; top:0; width:140px; height:190px;" role="img" aria-label="Model with long voluminous curled hair"></div>

    <div class="panel" style="left:145px; top:12px; width:140px; height:178px;">
      <div class="cols">
        <div>
          <p class="panel-title">best lace<br>closure</p>
          <table class="price-table">
            <tr><th>INCH</th><th>PRICES</th></tr>
            <tr><td>12</td><td>$64</td></tr><tr><td>14</td><td>$70</td></tr><tr><td>16</td><td>$78</td></tr>
            <tr><td>18</td><td>$86</td></tr><tr><td>20</td><td>$92</td></tr><tr><td>22</td><td>$102</td></tr>
            <tr><td>24</td><td>$104</td></tr>
          </table>
        </div>
        <div>
          <p class="panel-title">cheap lace<br>closure</p>
          <table class="price-table">
            <tr><th>INCH</th><th>PRICES</th></tr>
            <tr><td>10</td><td>$43</td></tr><tr><td>12</td><td>$48</td></tr><tr><td>14</td><td>$53</td></tr>
            <tr><td>16</td><td>$58</td></tr><tr><td>18</td><td>$62</td></tr><tr><td>20</td><td>$66</td></tr>
          </table>
        </div>
      </div>
    </div>

    <div class="panel" style="left:5px; top:196px; width:145px; height:138px;">
      <div class="cols">
        <div>
          <p class="panel-title">best lace<br>frontal 13*4</p>
          <table class="price-table">
            <tr><th>INCH</th><th>PRICES</th></tr>
            <tr><td>12</td><td>$172</td></tr><tr><td>14</td><td>$177</td></tr>
            <tr><td>16</td><td>$186</td></tr><tr><td>18</td><td>$203</td></tr>
          </table>
        </div>
        <div>
          <p class="panel-title">cheap lace<br>frontal 13*4</p>
          <table class="price-table">
            <tr><th>INCH</th><th>PRICES</th></tr>
            <tr><td>12</td><td>$120</td></tr><tr><td>14</td><td>$126</td></tr>
            <tr><td>16</td><td>$134</td></tr><tr><td>18</td><td>$142</td></tr>
          </table>
        </div>
      </div>
    </div>

    <div class="photo photo-blonde" style="left:155px; top:196px; width:135px; height:144px;" role="img" aria-label="Smiling model with long honey-blonde waves"></div>
  </div>
</section>

<section class="spread back" aria-label="Colour hair prices and notes">
  <div class="page">
    <div class="panel" style="left:8px; top:10px; width:92px; height:168px;">
      <p class="panel-title">solid color hair<br>straight and<br>body wave</p>
      <div class="cols">
        <table class="price-table">
          <tr><th>INCH</th><th>PRICES</th></tr>
          <tr><td>18</td><td>$63</td></tr><tr><td>20</td><td>$72</td></tr>
          <tr><td>22</td><td>$83</td></tr><tr><td>24</td><td>$90</td></tr>
        </table>
      </div>
    </div>
    <div class="panel" style="left:104px; top:10px; width:90px; height:168px;">
      <p class="panel-title" style="margin-top:18px;">deep wave</p>
      <div class="cols">
        <table class="price-table">
          <tr><th>INCH</th><th>PRICES</th></tr>
          <tr><td>18</td><td>$66</td></tr><tr><td>20</td><td>$75</td></tr>
          <tr><td>22</td><td>$86</td></tr><tr><td>24</td><td>$94</td></tr>
        </table>
      </div>
    </div>
    <div class="panel" style="left:198px; top:10px; width:94px; height:168px;">
      <p class="panel-title">ombre hair<br>straight and<br>body wave</p>
      <div class="cols">
        <table class="price-table">
          <tr><th>INCH</th><th>PRICES</th></tr>
          <tr><td>12</td><td>$50</td></tr><tr><td>14</td><td>$56</td></tr><tr><td>16</td><td>$67</td></tr>
          <tr><td>18</td><td>$74</td></tr><tr><td>20</td><td>$80</td></tr><tr><td>22</td><td>$88</td></tr>
          <tr><td>24</td><td>$98</td></tr>
        </table>
      </div>
    </div>
    <div class="photo photo-bag" style="left:14px; top:198px; width:82px; height:108px;" role="img" aria-label="Branded drawstring gift bag"></div>
    <p class="gift-note">free gift bag for loyal customers</p>
  </div>

  <div class="page">
    <p class="notes-title">Notes</p>
    <div class="notes-lines"></div>
    <p class="wordmark notes-mark">The Calder Range</p>
  </div>
</section>

</body>
</html>
```